Brightfield Claim Advisors Business Card

I would like to use the art developed in the logo project for my business to generate ideas for cool business cards.
I'm looking for something modern, yet sophisticated. I also want to use too many colors, and may want to print the cards on a metallic finish card stock, maybe a brush aluminum or metal.

Target Market(s)

I work with larger companies, and with executives and general counsels. Tends to be an older crowd, but with hip companies.

Industry/Entity Type

Business

Requirements
Should not have
• I'm not interested in generating any new designs, and don't want to overpower the logo already developed.

```html
<!DOCTYPE html>
<html lang="en">
<head>
<meta charset="utf-8">
<title>Brightfield Claim Advisors – Business Card</title>
<link rel="stylesheet" href="https://fonts.googleapis.com/css2?family=Exo+2:wght@400;500&family=Roboto:wght@400&display=swap">
<style>
  :root {
    --backdrop: #7a4632;
    --card: #232123;
    --accent: #f0732a;
    --brand-grey: #8a8a8c;
    --contact-grey: #9a999b;
    --white: #f4f4f4;
  }
  html, body {
    margin: 0;
    padding: 0;
    width: 1200px;
    height: 897px;
    overflow: hidden;
    background: var(--backdrop);
  }
  .card {
    position: absolute;
    left: 120px;
    top: 181px;
    width: 960px;
    height: 534px;
    background: var(--card);
    border-radius: 26px;
    box-shadow: 0 14px 30px rgba(0, 0, 0, 0.45);
  }
  .brand-dot {
    position: absolute;
    left: 190px;
    top: 88px;
    width: 146px;
    height: 146px;
    border-radius: 50%;
    background: var(--accent);
  }
  .brand-name {
    position: absolute;
    left: 390px;
    top: 92px;
    margin: 0;
    font-family: "Exo 2", sans-serif;
    font-weight: 500;
    font-size: 54px;
    line-height: 51px;
    letter-spacing: 1px;
    text-transform: uppercase;
    color: var(--brand-grey);
  }
  .brand-name .entity {
    font-size: 24px;
    letter-spacing: 1px;
  }
  .contact {
    position: absolute;
    left: 132px;
    top: 334px;
    margin: 0;
    padding: 0;
    list-style: none;
    font-family: "Roboto", sans-serif;
    font-size: 21px;
    line-height: 26.5px;
    color: var(--contact-grey);
  }
  .contact li {
    display: flex;
    align-items: center;
    height: 26.5px;
  }
  .contact .icon {
    width: 16px;
    height: 16px;
    margin-right: 12px;
    flex: none;
  }
  .contact .no-icon { margin-left: 28px; }
  .contact .web { color: var(--accent); }
  .person {
    position: absolute;
    right: 122px;
    top: 352px;
    text-align: right;
    font-family: "Exo 2", sans-serif;
  }
  .person-name {
    margin: 0;
    font-weight: 400;
    font-size: 44px;
    line-height: 48px;
    letter-spacing: 1px;
    color: var(--accent);
  }
  .person-role {
    margin: 0;
    font-weight: 400;
    font-size: 23px;
    line-height: 24px;
    color: var(--white);
  }
</style>
</head>
<body>
  <article class="card">
    <div class="brand-dot"></div>
    <h1 class="brand-name">Brightfield<br>Claim<br>Advisors<span class="entity">, PLLC</span></h1>

    <ul class="contact">
      <li>
        <svg class="icon" viewBox="0 0 16 16" aria-hidden="true"><path d="M8 1a5 5 0 0 0-5 5c0 3.6 5 9 5 9s5-5.4 5-9a5 5 0 0 0-5-5zm0 7a2 2 0 1 1 0-4 2 2 0 0 1 0 4z" fill="var(--accent)"/></svg>
        Address line 1
      </li>
      <li><span class="no-icon">Address line 2</span></li>
      <li>
        <svg class="icon" viewBox="0 0 16 16" aria-hidden="true"><rect x="4.5" y="1" width="7" height="14" rx="1.5" fill="none" stroke="var(--accent)" stroke-width="1.6"/><rect x="7" y="12" width="2" height="1.4" fill="var(--accent)"/></svg>
        000 000 000
      </li>
      <li>
        <svg class="icon" viewBox="0 0 16 16" aria-hidden="true"><rect x="1.5" y="4" width="13" height="9" fill="var(--accent)"/><path d="M1.5 4 8 9l6.5-5" fill="none" stroke="var(--card)" stroke-width="1.4"/></svg>
        dreyes@brightfield.com
      </li>
      <li class="web">
        <svg class="icon" viewBox="0 0 16 16" aria-hidden="true"><g fill="none" stroke="var(--accent)" stroke-width="1.3"><circle cx="8" cy="8" r="6.5"/><ellipse cx="8" cy="8" rx="2.8" ry="6.5"/><path d="M1.5 8h13M2.6 4.6h10.8M2.6 11.4h10.8"/></g></svg>
        www.brightfield.com
      </li>
    </ul>

    <div class="person">
      <p class="person-name">Daniel Reyes</p>
      <p class="person-role">SEO</p>
    </div>
  </article>
</body>
</html>
```